Compass & Canvas needs new business card design

I need a new business card design. I'm looking for out-of-the-box design which represents the freedom of being a location independent entrepreneur.
I offer coaching, retreats and trips.
I would like to see designs with and without the photo.
Colors I use are black (#000000), green (#25A796) and brown (#D7C38C)
Website compassandcanvas.net

Target Market(s)

location independent entrepreneurs, digital nomads, people looking to swap the 9 to 5 for a lifestyle business

Industry/Entity Type

Business

Contact Information for Business Card

Daria Tolsen
Your Lifestyle Business Coach, Retreat & Trip Leader
http://compassandcanvas.net
hello@compassandcanvas.net
Live a life you don't need a holiday from

Font styles to use
Serif
Sans Serif

Requirements
Must have
• One side should contain only the logo. I would also consider having the "Live a life you don't need a holiday from" on that side too (depending on how it looks)
• Please show both sides on the designs.

```html
<!DOCTYPE html>
<html lang="en">
<head>
<meta charset="utf-8">
<title>Compass &amp; Canvas — Business Card</title>
<link href="https://fonts.googleapis.com/css2?family=Source+Sans+3:ital,wght@0,400;0,600;1,600&display=swap" rel="stylesheet">
<style>
  :root {
    --page-bg: #000000;
    --card-bg: #343437;
    --ink: #f2f2f2;
    --accent: #25a796;
    --rule: #8a8a8d;
    --divider: #4a4a4e;
  }
  html, body {
    margin: 0;
    padding: 0;
    width: 1200px;
    height: 900px;
    overflow: hidden;
    background: var(--page-bg);
    font-family: "Source Sans 3", "Myriad Pro", Arial, sans-serif;
  }
  .canvas {
    position: relative;
    width: 1200px;
    height: 900px;
  }
  .card {
    position: absolute;
    top: 271px;
    width: 456px;
    height: 281px;
    border-radius: 14px;
    background: var(--card-bg);
    overflow: hidden;
  }
  .card--front { left: 137px; }
  .card--back { left: 626px; }

  .brand-name {
    position: absolute;
    margin: 0;
    color: var(--ink);
    font-weight: 600;
    letter-spacing: 0.04em;
    text-transform: uppercase;
    white-space: nowrap;
    transform: translate(-50%, -50%);
  }
  .card--front .brand-name {
    left: 116px;
    top: 138px;
    font-size: 19px;
  }
  .card--back .brand-name {
    left: 228px;
    top: 138px;
    font-size: 32px;
  }

  .divider {
    position: absolute;
    left: 211px;
    top: 80px;
    width: 1px;
    height: 115px;
    background: var(--divider);
  }

  .contact {
    position: absolute;
    left: 231px;
    top: 84px;
    color: var(--ink);
    font-size: 13px;
    line-height: 16px;
  }
  .contact__name {
    margin: 0 0 4px;
    color: var(--accent);
    font-size: 16px;
    font-weight: 600;
    line-height: 20px;
  }
  .contact__role { margin: 0; }
  .contact__links {
    list-style: none;
    margin: 20px 0 0;
    padding: 0;
  }
  .contact__links li {
    display: flex;
    align-items: center;
    gap: 5px;
    height: 17px;
  }
  .contact__links svg {
    width: 9px;
    height: 9px;
    flex: none;
  }

  .tagline {
    position: absolute;
    left: 0;
    right: 0;
    top: 235px;
    display: flex;
    align-items: center;
    gap: 14px;
    color: var(--ink);
    font-size: 14px;
    font-style: italic;
    font-weight: 600;
    white-space: nowrap;
  }
  .tagline::before,
  .tagline::after {
    content: "";
    flex: 1;
    height: 1px;
    background: var(--rule);
  }
</style>
</head>
<body>
<main class="canvas">
  <section class="card card--front" aria-label="Card front">
    <p class="brand-name">Compass &amp; Canvas</p>
    <div class="divider"></div>
    <div class="contact">
      <p class="contact__name">Daria Tolsen</p>
      <p class="contact__role">Your Lifestyle Business Coach</p>
      <p class="contact__role">Retreat &amp; Trip Leader</p>
      <ul class="contact__links">
        <li>
          <svg viewBox="0 0 10 10" aria-hidden="true"><rect x="0.5" y="1.5" width="9" height="7" fill="var(--accent)"/><path d="M0.5 1.5 L5 5.5 L9.5 1.5" fill="none" stroke="var(--card-bg)" stroke-width="1"/></svg>
          <span>hello@compassandcanvas.net</span>
        </li>
        <li>
          <svg viewBox="0 0 10 10" aria-hidden="true"><circle cx="5" cy="5" r="4.5" fill="var(--accent)"/><path d="M0.5 5 H9.5 M5 0.5 C2.5 3 2.5 7 5 9.5 M5 0.5 C7.5 3 7.5 7 5 9.5" fill="none" stroke="var(--card-bg)" stroke-width="0.7"/></svg>
          <span>www.compassandcanvas.net</span>
        </li>
      </ul>
    </div>
    <p class="tagline">Live a life you don't need a holiday from</p>
  </section>

  <section class="card card--back" aria-label="Card back">
    <p class="brand-name">Compass &amp; Canvas</p>
  </section>
</main>
</body>
</html>
```